U.S. Popcorn company needs business cards

We are a popcorn company that manufactures popcorn and sells it to grocery stores worldwide. Our theme is "Americana" and our logo is Kettle Mesa Byway which is the most famous highway in the U.S.

We would like the design to be simple and to use both sides. On the back side we would like to see just the logo and website. The front would be normal details

Target Market(s)

Wholesalers, grocers and distributors

Industry/Entity Type

Manufacture

Contact Information for Business Card

Business name: Kettle Mesa Popcorn
Phone: +1 555 014 2286
Email: Dale@kettlemesapopcorn.com
website: www.kettlemesapopcorn.com
Tag Line: "Fresh from the kettle"
Name: Dale Whitcombe
Title: Founder/President

Requirements
Must have
• Either this design should be fun or clean and simple. I will let you show me your thougths.
Nice to have
• Anything that ties in the real Kettle Mesa Byway.
• Colors might need to be red, white and blue incorporated.
Should not have
• Not be too busy.

```html
<!DOCTYPE html>
<html lang="en">
<head>
<meta charset="utf-8">
<title>Kettle Mesa Popcorn – Business Cards</title>
<link rel="stylesheet" href="https://fonts.googleapis.com/css2?family=Lato:wght@400;700;900&family=Short+Stack&display=swap">
<style>
  :root {
    --page: #ececec;
    --card: #ffffff;
    --navy: #0c2a6b;
    --red: #e21f26;
    --ink: #1d1d1d;
    --white: #ffffff;
  }
  * { margin: 0; padding: 0; box-sizing: border-box; }
  html, body {
    width: 1200px; height: 586px; overflow: hidden;
    background: var(--page);
    font-family: "Lato", Arial, sans-serif;
    color: var(--ink);
  }
  .card {
    position: absolute;
    top: 128px;
    width: 502px; height: 302px;
    background: var(--card);
    overflow: hidden;
  }
  .card--back { left: 61px; }
  .card--front { left: 619px; }

  .brand {
    position: absolute;
    display: flex; flex-direction: column; align-items: center;
    text-align: center;
  }
  .brand__dot {
    width: 40px; height: 40px; border-radius: 50%;
    background: var(--red);
    margin-bottom: 14px;
  }
  .brand__name {
    font-weight: 900;
    color: var(--navy);
    text-transform: uppercase;
    line-height: 1.05;
  }
  .card--back .brand { left: 0; width: 100%; top: 62px; }
  .card--back .brand__name { font-size: 36px; }
  .card--front .brand { left: 270px; width: 200px; top: 80px; }
  .card--front .brand__name { font-size: 27px; }

  .tagline {
    position: absolute; left: 0; width: 100%; top: 255px;
    text-align: center;
    font-family: "Short Stack", "Comic Sans MS", cursive;
    font-size: 11.5px; letter-spacing: 2px;
    color: var(--ink);
  }

  .bands { position: absolute; left: 0; bottom: 0; width: 502px; height: 14px; }

  .person { position: absolute; left: 36px; top: 40px; }
  .person__name { font-size: 16.5px; font-weight: 900; color: var(--red); }
  .person__title { font-size: 11.5px; margin-top: 4px; }

  .contact-tab {
    position: absolute; left: 0; top: 162px;
    width: 42px; height: 101px;
    background: var(--red);
    border-radius: 0 9px 9px 0;
  }
  .contact-tab svg { position: absolute; left: 13px; width: 16px; height: 16px; }
  .contact-list { position: absolute; left: 54px; top: 174px; list-style: none; }
  .contact-list li { font-size: 12.5px; font-weight: 700; height: 30px; line-height: 16px; }
</style>
</head>
<body>

  <section class="card card--back" aria-label="Card back">
    <div class="brand">
      <span class="brand__dot"></span>
      <span class="brand__name">Kettle Mesa<br>Popcorn</span>
    </div>
    <p class="tagline">Fresh from the kettle</p>
    <svg class="bands" viewBox="0 0 502 14" preserveAspectRatio="none">
      <rect x="0" y="2" width="320" height="12" fill="var(--navy)"/>
      <path d="M296 14 C302 5 308 1 322 1 L502 1 L502 14 Z" fill="var(--white)"/>
      <path d="M302 14 C308 4 314 0 326 0 L502 0 L502 14 Z" fill="var(--red)"/>
    </svg>
  </section>

  <section class="card card--front" aria-label="Card front">
    <div class="person">
      <h1 class="person__name">Dale Whitcombe</h1>
      <p class="person__title">Founder/President</p>
    </div>

    <div class="contact-tab">
      <svg style="top:12px" viewBox="0 0 16 16" aria-hidden="true">
        <path d="M3 2 L6 2 L7 5 L5 6.5 C6 8.5 7.5 10 9.5 11 L11 9 L14 10 L14 13 C14 14 13 14.5 12 14.5 C6.5 14 2 9.5 1.5 4 C1.5 3 2 2 3 2 Z" fill="var(--white)"/>
      </svg>
      <svg style="top:43px" viewBox="0 0 16 16" aria-hidden="true">
        <rect x="1" y="3" width="14" height="10" fill="var(--white)"/>
        <path d="M1.5 3.5 L8 9 L14.5 3.5" fill="none" stroke="var(--red)" stroke-width="1.2"/>
      </svg>
      <svg style="top:73px" viewBox="0 0 16 16" aria-hidden="true">
        <g fill="none" stroke="var(--white)" stroke-width="2" stroke-linecap="round">
          <path d="M7 9.5 L4.5 12 A2 2 0 0 1 2 9.5 L4.5 7"/>
          <path d="M9 6.5 L11.5 4 A2 2 0 0 1 14 6.5 L11.5 9"/>
          <path d="M6 10 L10 6"/>
        </g>
      </svg>
    </div>

    <ul class="contact-list">
      <li>+1 555 014 2286</li>
      <li>Dale@kettlemesapopcorn.com</li>
      <li>www.kettlemesapopcorn.com</li>
    </ul>

    <div class="brand">
      <span class="brand__dot"></span>
      <span class="brand__name">Kettle Mesa<br>Popcorn</span>
    </div>

    <svg class="bands" viewBox="0 0 502 14" preserveAspectRatio="none">
      <rect x="0" y="2" width="320" height="12" fill="var(--navy)"/>
      <path d="M296 14 C302 5 308 1 322 1 L502 1 L502 14 Z" fill="var(--white)"/>
      <path d="M302 14 C308 4 314 0 326 0 L502 0 L502 14 Z" fill="var(--red)"/>
    </svg>
  </section>

</body>
</html>
```